Business Card Design for boarding house accomodation business

I need a business card design for my Sydney based boarding house business accomodation. providing rooms for rent in Sydney Australia with shard bathroom and kitchen.
The front of card, are my details with details of head office and the rear of card to have details of locations providing rooms for rent.

Industry/Entity Type

Business

Contact Information for Business Card

Front of card details:
HOLLOWAY MANAGEMENT PTY LTD t/a
LINDFIELD'S GUEST HOUSE
ABN:52907318460
Daniel Kavanagh
48 Clement st
Newtown 2042
Mobile:0417386920
Email:daniel@lindfieldsguesthouse.example.au

Back of Card:
Locations:
-48 Clement st
Newtown 2042

-362 Harlow st
Erskineville 2043

-87 Fenwick st
Bondi 2026

-294 Ashcombe rd
Marrickville 2043

```html
<!DOCTYPE html>
<html lang="en">
<head>
<meta charset="utf-8">
<title>Lindfield's Guest House – Business Card</title>
<link rel="stylesheet" href="https://fonts.googleapis.com/css2?family=Arimo:wght@400;700&family=Noto+Serif:wght@700&display=swap">
<style>
  :root {
    --canvas-bg: #e4e2de;
    --card-white: #f7f7f5;
    --ink: #1c1c1c;
    --band-light: #3da3c4;
    --band-mid: #1a7fa9;
    --band-dark: #0d6690;
    --frame-blue: #1d6e93;
    --on-band: #ffffff;
  }
  * { margin: 0; padding: 0; box-sizing: border-box; }
  html, body { width: 1200px; height: 892px; overflow: hidden; }
  body {
    background: var(--canvas-bg);
    font-family: "Arimo", Arial, sans-serif;
    color: var(--ink);
    position: relative;
  }
  .card {
    position: absolute;
    left: 250px;
    width: 700px;
    height: 400px;
    background: var(--card-white);
    box-shadow: 0 6px 18px rgba(0,0,0,.18);
    overflow: hidden;
  }
  .card--front { top: 26px; }
  .card--back { top: 466px; border: 7px solid var(--frame-blue); }

  .band { position: absolute; inset: 0; width: 100%; height: 100%; }

  .company {
    position: absolute; right: 34px; top: 34px;
    font-family: "Noto Serif", Georgia, serif; font-weight: 700;
    font-size: 34px; letter-spacing: .2px;
  }
  .trading-name {
    position: absolute; left: 150px; top: 84px;
    font-size: 17px; letter-spacing: .3px;
  }
  .abn {
    position: absolute; left: 30px; top: 156px;
    font-size: 15px; color: var(--on-band); opacity: .9;
  }
  .holder {
    position: absolute; right: 34px; top: 220px;
    font-family: "Noto Serif", Georgia, serif; font-weight: 700;
    font-size: 32px; color: var(--on-band);
  }
  .contact-list {
    position: absolute; right: 34px; top: 274px;
    list-style: none; text-align: right; color: var(--on-band);
    font-size: 18px; line-height: 30px;
  }
  .contact-list li { display: flex; justify-content: flex-end; align-items: center; gap: 10px; }
  .contact-list svg { width: 16px; height: 16px; fill: var(--on-band); }

  .locations-title {
    position: absolute; left: 90px; top: 56px;
    font-size: 30px; font-weight: 400;
  }
  .location-list {
    position: absolute; left: 80px; top: 118px;
    list-style: none; font-size: 24px; line-height: 50px;
  }
  .location-list li { display: flex; align-items: center; gap: 18px; }
  .location-list svg { width: 22px; height: 20px; fill: var(--ink); }
</style>
</head>
<body>

<section class="card card--front">
  <svg class="band" viewBox="0 0 700 400" preserveAspectRatio="none" aria-hidden="true">
    <defs>
      <linearGradient id="bandFill" x1="0" y1="0" x2="1" y2="1">
        <stop offset="0" stop-color="#3da3c4"/>
        <stop offset=".5" stop-color="#1a7fa9"/>
        <stop offset="1" stop-color="#0d6690"/>
      </linearGradient>
    </defs>
    <path d="M0,128 C230,118 480,138 700,192 L700,400 L0,400 Z" fill="url(#bandFill)"/>
  </svg>

  <h1 class="company">Holloway Management pty ltd</h1>
  <p class="trading-name">LINDFIELD'S GUEST HOUSE</p>
  <p class="abn">ABN:52907318460</p>
  <h2 class="holder">Daniel Kavanagh</h2>
  <ul class="contact-list">
    <li>0417386920
      <svg viewBox="0 0 16 16"><path d="M4 1h8a1 1 0 0 1 1 1v12a1 1 0 0 1-1 1H4a1 1 0 0 1-1-1V2a1 1 0 0 1 1-1zm1 2v8h6V3zm3 9.2a.9.9 0 1 0 0 1.8.9.9 0 0 0 0-1.8z"/></svg>
    </li>
    <li>daniel@lindfieldsguesthouse.example.au
      <svg viewBox="0 0 16 16"><path d="M1 3h14v10H1zm1.5 1.2L8 8.6l5.5-4.4zM2 5.4V12h12V5.4L8 10.2z"/></svg>
    </li>
    <li>48 Clement st&nbsp;&nbsp;Newtown 2042
      <svg viewBox="0 0 16 16"><path d="M8 1a5 5 0 0 1 5 5c0 3.6-5 9-5 9S3 9.6 3 6a5 5 0 0 1 5-5zm0 3a2 2 0 1 0 0 4 2 2 0 0 0 0-4z"/></svg>
    </li>
  </ul>
</section>

<section class="card card--back">
  <h2 class="locations-title">Locations ;</h2>
  <ul class="location-list">
    <li><svg viewBox="0 0 22 20"><path d="M11 1 1 10h3v9h5v-6h4v6h5v-9h3z"/></svg>48 Clement st&nbsp;&nbsp;Newtown 2042</li>
    <li><svg viewBox="0 0 22 20"><path d="M11 1 1 10h3v9h5v-6h4v6h5v-9h3z"/></svg>362 Harlow st&nbsp;&nbsp;Erskineville 2043</li>
    <li><svg viewBox="0 0 22 20"><path d="M11 1 1 10h3v9h5v-6h4v6h5v-9h3z"/></svg>87 Fenwick st&nbsp;&nbsp;Bondi 2026</li>
    <li><svg viewBox="0 0 22 20"><path d="M11 1 1 10h3v9h5v-6h4v6h5v-9h3z"/></svg>294 Ashcombe rd&nbsp;&nbsp;Marrickville 2043</li>
  </ul>
</section>

</body>
</html>
```